I am hosting a banquet called, Copper Meadow Gala and I need a design to help sell it on Friendlane.

Hi all.
No disco balls, please.
I would like a miser-traditional design, classy.

```html
<!DOCTYPE html>
<html lang="en">
<head>
<meta charset="utf-8">
<title>Copper Meadow Gala – Invitation</title>
<link rel="stylesheet" href="https://fonts.googleapis.com/css2?family=Playfair+Display:wght@400;500;600&family=Poppins:wght@400&family=Great+Vibes&display=swap">
<style>
  :root {
    --ink: #1b1b1b;
    --paper: #ffffff;
    --muted: #8c8c8c;
    --split: 522px;
  }
  * { margin: 0; padding: 0; box-sizing: border-box; }
  html, body { width: 1200px; height: 1200px; overflow: hidden; background: var(--paper); }
  .invite {
    position: relative; width: 1200px; height: 1200px; overflow: hidden;
    background: linear-gradient(to right, var(--ink) 0 var(--split), var(--paper) var(--split) 100%);
    font-family: "Poppins", sans-serif;
  }
  .heading-layer { position: absolute; inset: 0; }
  .heading-layer.on-dark { color: var(--paper); clip-path: inset(0 calc(1200px - var(--split)) 0 0); }
  .heading-layer.on-light { color: var(--ink); clip-path: inset(0 0 0 var(--split)); }
  .heading-layer > * { position: absolute; left: 0; right: 0; text-align: center; line-height: 1; white-space: nowrap; }
  .occasion { top: 94px; font-size: 30px; letter-spacing: 6px; }
  .event-title { top: 172px; font-family: "Playfair Display", serif; font-weight: 600; font-size: 94px; letter-spacing: -1px; }
  .host { top: 274px; font-size: 45px; }
  .invite-line { top: 370px; font-family: "Great Vibes", cursive; font-size: 84px; }

  .abs { position: absolute; line-height: 1; white-space: nowrap; }
  .serif { font-family: "Playfair Display", serif; }

  .day-name { left: 119px; top: 526px; font-size: 38px; letter-spacing: 4px; color: var(--paper); }
  .date-badge {
    left: 124px; top: 588px; width: 106px; height: 106px; border-radius: 50%;
    background: var(--paper); color: var(--ink); display: flex; align-items: center; justify-content: center;
    font-size: 46px;
  }
  .date-badge sup, .rsvp-badge sup { font-size: 0.5em; vertical-align: 0.8em; }
  .month { left: 247px; top: 588px; font-size: 46px; color: var(--paper); }
  .year { left: 246px; top: 646px; font-size: 52px; color: var(--muted); }
  .schedule { left: 119px; font-size: 34px; color: var(--paper); }
  .schedule.social { top: 784px; }
  .schedule.dinner { top: 869px; }
  .ticket-label { left: 119px; top: 1004px; font-size: 36px; line-height: 1.3; color: var(--paper); }
  .ticket-price { left: 272px; top: 990px; font-size: 104px; color: var(--paper); }
  .ticket-price sup { font-size: 0.42em; vertical-align: 1em; }

  .section-head { left: 553px; font-size: 40px; font-weight: 500; color: var(--ink); letter-spacing: -0.5px; }
  .section-head.venue { top: 524px; }
  .section-head.dress { top: 758px; }
  .detail { font-size: 29px; color: var(--ink); line-height: 1.45; }
  .detail.venue { left: 558px; top: 583px; }
  .detail.dress { left: 564px; top: 807px; }
  .divider { position: absolute; left: 560px; width: 418px; height: 14px; }
  .divider.first { top: 699px; }
  .divider.second { top: 933px; }

  .rsvp-label { left: 556px; top: 996px; font-size: 34px; color: var(--ink); }
  .rsvp-row { position: absolute; left: 556px; top: 1028px; height: 96px; display: flex; align-items: center; color: var(--ink); }
  .rsvp-row .part { font-family: "Playfair Display", serif; font-size: 44px; line-height: 1; }
  .rsvp-row .rule { width: 1.5px; height: 66px; background: var(--ink); margin: 0 18px; }
  .rsvp-row .month-part { display: flex; align-items: center; gap: 10px; margin-top: 8px; }
  .rsvp-badge {
    width: 96px; height: 96px; border-radius: 50%; background: var(--ink); color: var(--paper);
    display: flex; align-items: center; justify-content: center; font-family: "Playfair Display", serif; font-size: 38px;
  }
</style>
</head>
<body>
<main class="invite">
  <div class="heading-layer on-dark" aria-hidden="true">
    <p class="occasion">Alder Creek Centennial</p>
    <h1 class="event-title">Copper Meadow Gala</h1>
    <p class="host">Alder Creek Chamber of Commerce</p>
    <p class="invite-line">Join us for the Celebration</p>
  </div>
  <div class="heading-layer on-light">
    <p class="occasion">Alder Creek Centennial</p>
    <h1 class="event-title">Copper Meadow Gala</h1>
    <p class="host">Alder Creek Chamber of Commerce</p>
    <p class="invite-line">Join us for the Celebration</p>
  </div>

  <p class="abs serif day-name">SATURDAY</p>
  <div class="abs serif date-badge">3<sup>rd</sup></div>
  <p class="abs serif month">June</p>
  <p class="abs serif year">2023</p>
  <p class="abs serif schedule social">Social Hour 6:00 p.m.</p>
  <p class="abs serif schedule dinner">Dinner 7:00 p.m.</p>
  <p class="abs ticket-label">TICKET<br>PRICE</p>
  <p class="abs serif ticket-price"><sup>$</sup>30</p>

  <h2 class="abs serif section-head venue">VENUE</h2>
  <p class="abs detail venue">Alder Creek High School Gymnasium<br>418 Mercer Street, Alder Creek, Kansas</p>
  <svg class="divider first" viewBox="0 0 418 14" aria-hidden="true">
    <line x1="6" y1="7" x2="412" y2="7" stroke="#1b1b1b" stroke-width="1.5"/>
    <path d="M2 7 L7 3 L12 7 L7 11Z M406 7 L411 3 L416 7 L411 11Z" fill="#1b1b1b"/>
    <circle cx="209" cy="7" r="3" fill="#1b1b1b"/>
  </svg>
  <h2 class="abs serif section-head dress">DRESS CODE:</h2>
  <p class="abs detail dress">Black &amp; White Attire<br>Smart Casual to Fancy Formal</p>
  <svg class="divider second" viewBox="0 0 418 14" aria-hidden="true">
    <line x1="6" y1="7" x2="412" y2="7" stroke="#1b1b1b" stroke-width="1.5"/>
    <path d="M2 7 L7 3 L12 7 L7 11Z M406 7 L411 3 L416 7 L411 11Z" fill="#1b1b1b"/>
    <circle cx="209" cy="7" r="3" fill="#1b1b1b"/>
  </svg>

  <p class="abs rsvp-label">RSVP</p>
  <div class="rsvp-row">
    <span class="part">Monday</span>
    <span class="rule"></span>
    <span class="month-part"><span class="part">May</span><span class="rsvp-badge">29<sup>th</sup></span></span>
    <span class="rule"></span>
    <span class="part">2023</span>
  </div>
</main>
</body>
</html>
```